Business card design needed

Front of Card:
I would like to have nearly 3/4 of the card from the top in a Pea Green Colour with the word 'Lanternfield' written in a(Watermelon Red colour) in the font 'Viner Hand ITC'. Lanternfield to be written within the Green colour of the card.

The lower 1/3 of the card I would like to have white with the words:
Home and Garden Styling smaller than the word Lanternfield in Black in the font 'Batang', centred underneath the green section.

At the very bottom in one corner in smaller print I would like to have my contact phone number: Pip M:0437960214 and then the email address:
E: lanternfieldstyling@quobnet.net.au on the other side.

Back of Card:
Back of Card to be White
On one side (Left)
I would like the Heading "Garden" in the same pea green colour as the front and in the Viner Hand ITC font. On the other half of the card I would like 'Home' in the Watermelon Red Colour (same as front colour) and in the font Viner Hand ITC.
Underneath these Headings I would like written in black and in Batang font the following list of services.

Garden Home
Garden Styling Interior Styling
Plant Selection Furniture Selection/Arrangement Garden Maintenance Setting Up Home (after move)
Hedging/Mowing Merchandise and Stylist for
Work w/Local Nurseries Brenna and Hask

Lanternfield
Home and Garden Styling
M: 0437960214 E: lanternfieldstyling@quobnet.net.au

```html
<!DOCTYPE html>
<html lang="en">
<head>
<meta charset="utf-8">
<title>Lanternfield Home and Garden Styling – Business Card</title>
<link rel="stylesheet" href="https://fonts.googleapis.com/css2?family=Kalam:wght@400&family=Gowun+Batang&display=swap">
<style>
  :root {
    --pea-green: #22c22a;
    --pea-green-light: #3fd445;
    --watermelon: #e0341c;
    --ink: #1e1e1e;
    --paper: #ffffff;
    --paper-shade: #ececec;
    --backdrop: #3a3a3a;
    --hand: "Kalam", cursive;
    --serif: "Gowun Batang", serif;
  }
  * { margin: 0; padding: 0; box-sizing: border-box; }
  html, body { width: 1200px; height: 1000px; overflow: hidden; }
  body {
    background: var(--backdrop);
    display: flex;
    flex-direction: column;
    align-items: center;
    justify-content: center;
    gap: 30px;
  }
  .card {
    position: relative;
    width: 820px;
    height: 455px;
    background: linear-gradient(180deg, var(--paper) 60%, var(--paper-shade));
    overflow: hidden;
    box-shadow: 0 6px 18px rgba(0,0,0,0.45);
  }

  /* Front */
  .front-field {
    position: absolute; left: 0; top: 0; width: 100%; height: 262px;
    background: radial-gradient(ellipse at 45% 30%, var(--pea-green-light), var(--pea-green) 70%);
  }
  .fence-border {
    position: absolute; left: 0; top: 250px; width: 100%; height: 56px;
    background: linear-gradient(180deg, var(--pea-green) 0%, var(--pea-green) 35%, var(--paper) 100%);
  }
  .brand-name {
    position: absolute; left: 0; right: 0; top: 70px;
    text-align: center;
    font-family: var(--hand);
    font-size: 104px;
    line-height: 1;
    color: var(--watermelon);
  }
  .tagline {
    position: absolute; left: 0; right: 0; top: 322px;
    text-align: center;
    font-family: var(--serif);
    font-size: 24px;
    letter-spacing: 0.55em;
    color: var(--ink);
  }
  .front-email {
    position: absolute; right: 34px; top: 370px;
    font-family: var(--serif); font-size: 20px; color: var(--ink);
  }
  .front-phone {
    position: absolute; left: 34px; top: 410px;
    font-family: var(--serif); font-size: 20px; color: var(--ink);
    word-spacing: 0.3em;
  }

  /* Back */
  .back-panel { position: absolute; left: 0; top: 0; }
  .back-heading {
    position: absolute; top: 170px; width: 390px;
    text-align: center;
    font-family: var(--hand);
    font-size: 78px;
    line-height: 1;
  }
  .back-heading--home { left: 0; color: var(--watermelon); }
  .back-heading--garden { left: 420px; width: 400px; color: var(--pea-green); }
  .service-list {
    position: absolute; left: 18px; top: 318px;
    list-style: none;
    font-family: var(--serif); font-size: 12.5px; line-height: 1.35;
    color: var(--ink);
  }
  .service-list li::before { content: "– "; }
  .back-contact {
    position: absolute; left: 450px; top: 360px;
    font-family: var(--serif); font-size: 16px; line-height: 1.3;
    color: var(--ink);
  }
</style>
</head>
<body>

  <section class="card card--front" aria-label="Card front">
    <div class="front-field"></div>
    <div class="fence-border" role="img" aria-label="White picket fence border along the edge of the green field"></div>
    <h1 class="brand-name">Lanternfield</h1>
    <p class="tagline">Home and Garden Styling</p>
    <p class="front-email">lanternfieldstyling@quobnet.net.au</p>
    <p class="front-phone">Pip M : 0437960214</p>
  </section>

  <section class="card card--back" aria-label="Card back">
    <svg class="back-panel" width="820" height="455" viewBox="0 0 820 455" aria-hidden="true">
      <polygon fill="var(--pea-green)" points="0,0 380,0 420,22.75 380,45.5 420,68.25 380,91 420,113.75 380,136.5 420,159.25 380,182 420,204.75 380,227.5 420,250.25 380,273 420,295.75 380,318.5 420,341.25 380,364 420,386.75 380,409.5 420,432.25 380,455 0,455"/>
    </svg>
    <h2 class="back-heading back-heading--home">Home</h2>
    <h2 class="back-heading back-heading--garden">Garden</h2>
    <ul class="service-list">
      <li>Garden Home</li>
      <li>Garden Styling Interior Styling</li>
      <li>Plant Selection Furniture Selection/</li>
      <li>Arrangement Garden Maintenance</li>
      <li>Setting Up Home (after move)</li>
      <li>Hedging/Mowing Merchandise and Stylist for</li>
      <li>Work w/Local Nurseries Brenna and Hask</li>
    </ul>
    <div class="back-contact">
      <p>Lanternfield Home and Garden Styling</p>
      <p>M: 0437960214</p>
      <p>E: lanternfieldstyling@quobnet.net.au</p>
    </div>
  </section>

</body>
</html>
```